Quill And Ferry Business Card

I need a business card designed around my logo (which was designed here on Sketch Forum!)

Target Market(s)

Professional Businesses

Industry/Entity Type

Business

Requirements
Must have
• Details that must be on the business card:

Renata Ovalle
Director
0491 253 608
renata@quillandferry.com.au
www.quillandferry.com.au
PO Box 4720 Brambleton Tas 7015

```html
<!DOCTYPE html>
<html lang="en">
<head>
<meta charset="utf-8">
<title>Quill And Ferry Business Card</title>
<link rel="stylesheet" href="https://fonts.googleapis.com/css2?family=Marcellus&family=Montserrat:wght@400;600;700&display=swap">
<style>
  :root {
    --charcoal: #3a3a3c;
    --brand-red: #d0202a;
    --paper: #f7f7f5;
    --ink-grey: #4a4a4c;
    --stage: #e4e3df;
    --white: #ffffff;
  }
  * { margin: 0; padding: 0; box-sizing: border-box; }
  html, body { width: 1200px; height: 800px; overflow: hidden; }
  body {
    background: var(--stage);
    position: relative;
    font-family: "Montserrat", sans-serif;
  }
  .card {
    position: absolute;
    width: 560px;
    height: 320px;
    border-radius: 3px;
    box-shadow: 0 10px 24px rgba(0,0,0,0.18);
    overflow: hidden;
  }

  /* Front of card */
  .card-front {
    left: 150px;
    top: 150px;
    background: var(--charcoal);
  }
  .front-mark {
    position: absolute;
    left: 60px;
    top: 100px;
    width: 120px;
    height: 120px;
    background: var(--brand-red);
  }
  .front-name {
    position: absolute;
    right: 34px;
    top: 128px;
    font-family: "Marcellus", serif;
    font-size: 31px;
    letter-spacing: 1px;
    color: var(--white);
    text-transform: uppercase;
    white-space: nowrap;
  }
  .front-web {
    position: absolute;
    right: 34px;
    top: 196px;
    font-size: 13px;
    color: var(--white);
    letter-spacing: 0.3px;
  }

  /* Back of card */
  .card-back {
    left: 490px;
    top: 400px;
    background: var(--paper);
  }
  .back-brand {
    position: absolute;
    left: 56px;
    top: 62px;
    display: flex;
    align-items: center;
    gap: 18px;
  }
  .back-mark {
    width: 46px;
    height: 46px;
    background: var(--brand-red);
  }
  .back-name {
    font-family: "Marcellus", serif;
    font-size: 31px;
    letter-spacing: 1px;
    color: var(--charcoal);
    text-transform: uppercase;
    white-space: nowrap;
  }
  .person {
    position: absolute;
    left: 40px;
    bottom: 76px;
  }
  .person-name {
    font-size: 14px;
    font-weight: 700;
    color: var(--brand-red);
    text-transform: uppercase;
    letter-spacing: 0.3px;
  }
  .person-role {
    font-size: 11px;
    color: var(--ink-grey);
    margin-top: 2px;
  }
  .contact {
    position: absolute;
    right: 30px;
    bottom: 76px;
    text-align: right;
    font-size: 11.5px;
    color: var(--ink-grey);
    line-height: 1.65;
    white-space: nowrap;
  }
  .contact-label {
    color: var(--brand-red);
    font-weight: 700;
  }
  .back-band {
    position: absolute;
    left: 0;
    bottom: 26px;
    width: 560px;
    height: 22px;
  }
</style>
</head>
<body>

<section class="card card-front">
  <div class="front-mark"></div>
  <div class="front-name">Quill And Ferry</div>
  <div class="front-web">www.quillandferry.com.au</div>
</section>

<section class="card card-back">
  <div class="back-brand">
    <div class="back-mark"></div>
    <div class="back-name">Quill And Ferry</div>
  </div>

  <div class="person">
    <div class="person-name">Renata Ovalle</div>
    <div class="person-role">Director</div>
  </div>

  <div class="contact">
    <div>PO Box 4720 Brambleton Tas 7015</div>
    <div><span class="contact-label">T:</span> 0491 253 608 · <span class="contact-label">E:</span> renata@quillandferry.com.au</div>
  </div>

  <svg class="back-band" viewBox="0 0 560 22" aria-hidden="true">
    <polygon points="0,0 210,0 232,22 0,22" fill="var(--brand-red)"/>
    <polygon points="216,0 560,0 560,22 238,22" fill="var(--charcoal)"/>
  </svg>
</section>

</body>
</html>
```